Casa Vero Inspections Business Card

I need a business card for my new company. The company is going to provide home inspections. The name of the company is Casa Vero Inspections. I am not sure if I want a single sided card or a double. I have a logo already that I want to incorporate into the card design. I was wondering if I should incorporate a catch phrase on my card or not. If I did the phrase would be "Careful Eyes on Every Home You Buy" but i am unsure how or if to use it on a card. The following information needs to be on the card.
Home Inspection
My Name: Marcus T. Wolford Phone Number: 555-301-7762 Email: mwolford@casaveroinspections.com Website: www.casaveroinspections.com NY HI License # 27300519462

```html
<!DOCTYPE html>
<html lang="en">
<head>
<meta charset="utf-8">
<title>Casa Vero Inspections – Business Card</title>
<link rel="stylesheet" href="https://fonts.googleapis.com/css2?family=Montserrat:wght@500;700&family=Roboto:wght@400&display=swap">
<style>
  :root {
    --stage: #5a5a5a;
    --card-dark: #3b3b3b;
    --card-light: #f2f3f2;
    --brand-blue: #166db0;
    --sky-blue: #7cc8ee;
    --ink: #3d3d3d;
    --white: #ffffff;
    --muted: #c9c9c9;
  }
  * { box-sizing: border-box; margin: 0; padding: 0; }
  html, body { width: 1200px; height: 960px; overflow: hidden; }
  body {
    background: var(--stage);
    position: relative;
    font-family: "Roboto", sans-serif;
  }
  .card {
    position: absolute;
    top: 180px;
    width: 360px;
    height: 600px;
    border-radius: 44px;
    overflow: hidden;
  }
  .card--back { left: 150px; background: var(--card-dark); }
  .card--front { left: 690px; background: var(--card-light); }

  /* Back side */
  .back-brand {
    position: absolute;
    left: 20px; right: 20px; top: 250px;
    text-align: center;
  }
  .brand-name {
    font-family: "Montserrat", sans-serif;
    font-weight: 700;
    letter-spacing: 0.02em;
    line-height: 1.1;
  }
  .back-brand .brand-name { color: var(--white); font-size: 34px; }
  .tagline {
    margin-top: 14px;
    color: var(--muted);
    font-size: 10.5px;
    letter-spacing: 0.04em;
    text-transform: uppercase;
  }

  /* Front side */
  .side-band { position: absolute; left: 0; top: 0; width: 70px; height: 600px; }
  .license {
    position: absolute;
    left: 4px; bottom: 90px;
    transform-origin: left bottom;
    transform: rotate(-90deg) translate(0, 30px);
    color: var(--white);
    font-size: 15px;
    white-space: nowrap;
  }
  .front-brand {
    position: absolute;
    left: 70px; right: 20px; top: 110px;
    text-align: center;
  }
  .front-brand .brand-name { color: var(--brand-blue); font-size: 30px; }
  .brand-square {
    display: inline-block;
    width: 14px; height: 14px;
    background: var(--sky-blue);
    margin-bottom: 12px;
  }
  .person { position: absolute; left: 96px; right: 16px; top: 372px; }
  .person-name {
    font-family: "Montserrat", sans-serif;
    font-weight: 700;
    font-size: 20px;
    color: var(--brand-blue);
    text-transform: uppercase;
    white-space: nowrap;
  }
  .person-role {
    font-family: "Montserrat", sans-serif;
    font-weight: 500;
    font-size: 16px;
    color: var(--sky-blue);
    margin-top: 2px;
  }
  .contact { list-style: none; position: absolute; left: 96px; right: 14px; top: 460px; }
  .contact li {
    display: flex; align-items: center; gap: 8px;
    font-size: 13.5px; color: var(--ink);
    margin-bottom: 8px;
    white-space: nowrap;
  }
  .contact svg { width: 15px; height: 15px; flex: none; }
</style>
</head>
<body>
  <section class="card card--back" aria-label="Card back">
    <div class="back-brand">
      <p class="brand-name">CASA VERO<br>INSPECTIONS</p>
      <p class="tagline">Careful Eyes on Every Home You Buy</p>
    </div>
  </section>

  <section class="card card--front" aria-label="Card front">
    <svg class="side-band" viewBox="0 0 70 600" aria-hidden="true">
      <polygon points="0,0 34,0 34,290 0,310" fill="var(--sky-blue)"/>
      <polygon points="0,300 60,270 60,600 0,600" fill="var(--brand-blue)"/>
      <polygon points="34,0 70,0 70,600 60,600 60,270 34,290" fill="var(--card-light)"/>
    </svg>
    <p class="license">NY HI License # 27300519462</p>

    <div class="front-brand">
      <span class="brand-square" aria-hidden="true"></span>
      <p class="brand-name">CASA VERO<br>INSPECTIONS</p>
    </div>

    <div class="person">
      <p class="person-name">Marcus T. Wolford</p>
      <p class="person-role">Founder &amp; CEO</p>
    </div>

    <ul class="contact">
      <li>
        <svg viewBox="0 0 24 24" aria-hidden="true"><path fill="var(--brand-blue)" d="M6.6 10.8a15 15 0 0 0 6.6 6.6l2.2-2.2a1 1 0 0 1 1-.25 11.4 11.4 0 0 0 3.6.57 1 1 0 0 1 1 1V20a1 1 0 0 1-1 1A17 17 0 0 1 3 4a1 1 0 0 1 1-1h3.5a1 1 0 0 1 1 1c0 1.25.2 2.45.57 3.57a1 1 0 0 1-.25 1z"/></svg>
        555-301-7762
      </li>
      <li>
        <svg viewBox="0 0 24 24" aria-hidden="true"><rect x="2" y="5" width="20" height="14" fill="none" stroke="var(--brand-blue)" stroke-width="2"/><path d="M2 5l10 8 10-8" fill="none" stroke="var(--brand-blue)" stroke-width="2"/></svg>
        mwolford@casaveroinspections.com
      </li>
      <li>
        <svg viewBox="0 0 24 24" aria-hidden="true"><g fill="none" stroke="var(--brand-blue)" stroke-width="1.6"><circle cx="12" cy="12" r="10"/><ellipse cx="12" cy="12" rx="4.5" ry="10"/><path d="M2 12h20M4 7h16M4 17h16"/></g></svg>
        www.casaveroinspections.com
      </li>
    </ul>
  </section>
</body>
</html>
```